The City of Ashford Vale needs a cover for their 2020 Activities Guide

Good morning.

My name is Darren Kellaway. I am the new Executive Assistant to City Manager P. Warren Lusk in the City of Ashford Vale. In the past my predecessor, Cody Brandt has reached out to you for different projects.

I am reaching out for another project – the cover of our 2020 Activity Guide. This Activity Guide will have the different activities to do in the City of Ashford Vale for 2020.

I have attached a draft sketch of what we would like to do and an in-depth explanation of what we would like.

```html
<!DOCTYPE html>
<html lang="en">
<head>
<meta charset="utf-8">
<title>City of Ashford Vale – 2020 Activity Guide Cover</title>
<link href="https://fonts.googleapis.com/css2?family=Roboto+Condensed:wght@700;800&family=Roboto:wght@700&display=swap" rel="stylesheet">
<style>
  :root {
    --page-bg: #e6e4e1;
    --navy: #1b2a8a;
    --navy-deep: #101a5e;
    --silver-light: #f4f4f5;
    --silver-mid: #d9dadd;
    --silver-dark: #a9abb0;
    --ink: #111111;
    --white: #ffffff;
    --seal-yellow: #f2c72c;
  }
  * { box-sizing: border-box; margin: 0; padding: 0; }
  html, body {
    width: 1200px; height: 1079px; overflow: hidden;
    background: var(--page-bg);
  }
  .cover {
    position: absolute; left: 230px; top: 20px;
    width: 740px; height: 1040px;
    background: linear-gradient(180deg, var(--silver-light) 0%, #ececee 50%, var(--silver-mid) 100%);
    box-shadow: 0 6px 18px rgba(0,0,0,.25);
    overflow: hidden;
    font-family: "Roboto Condensed", "Arial Narrow", sans-serif;
  }
  .cover-art { position: absolute; inset: 0; }
  .city-mark {
    position: absolute; left: 40px; top: 18px; width: 180px;
    display: flex; flex-direction: column; align-items: center; gap: 10px;
  }
  .city-mark__circle {
    width: 118px; height: 118px; border-radius: 50%;
    background: var(--seal-yellow);
  }
  .city-mark__name {
    color: var(--white); font-weight: 700; font-size: 16px;
    letter-spacing: .5px; text-transform: uppercase; white-space: nowrap;
  }
  .title {
    position: absolute; left: 236px; top: 40px; width: 410px;
    color: var(--white); text-align: center; font-weight: 800; line-height: 1;
  }
  .title__year { display: block; font-size: 74px; letter-spacing: .5px; }
  .title__sub { display: block; font-size: 46px; margin-top: 6px; }
  .footer-heading {
    position: absolute; left: 0; top: 930px; width: 740px;
    text-align: center; color: var(--white);
    font-weight: 800; font-size: 32px;
  }
  .contact-pill {
    position: absolute; top: 978px; height: 28px;
    border-radius: 14px;
    background: linear-gradient(180deg, #f2f2f3, var(--silver-dark));
    display: flex; align-items: center; justify-content: center; gap: 8px;
    font-family: "Roboto", Arial, sans-serif; font-weight: 700; font-size: 14px;
    color: var(--ink);
  }
  .contact-pill--web { left: 98px; width: 216px; }
  .contact-pill--phone { left: 420px; width: 222px; }
  .contact-pill svg { width: 15px; height: 15px; }
</style>
</head>
<body>
<main class="cover">
  <svg class="cover-art" width="740" height="1040" viewBox="0 0 740 1040" aria-hidden="true">
    <defs>
      <linearGradient id="navyBand" x1="0" y1="0" x2="0" y2="1">
        <stop offset="0" stop-color="var(--navy-deep)"/>
        <stop offset="1" stop-color="var(--navy)"/>
      </linearGradient>
      <radialGradient id="discFace" cx=".4" cy=".35" r=".7">
        <stop offset="0" stop-color="#ffffff"/>
        <stop offset="1" stop-color="#d8d9dc"/>
      </radialGradient>
      <filter id="discShadow" x="-30%" y="-30%" width="160%" height="160%">
        <feDropShadow dx="0" dy="2" stdDeviation="1.6" flood-color="#000" flood-opacity=".3"/>
      </filter>
      <clipPath id="gridClip"><rect x="45" y="240" width="646" height="640"/></clipPath>

      <circle id="disc" r="19" fill="url(#discFace)" filter="url(#discShadow)"/>

      <!-- activity tokens -->
      <g id="t0"><use href="#disc"/></g>
      <g id="t1"><use href="#disc"/></g>
      <g id="t2"><use href="#disc"/><path d="M-12 6 L-5 -4 L-1 1 L5 -7 L12 6" fill="none" stroke="var(--ink)" stroke-width="1"/></g>
      <g id="t3"><use href="#disc"/><circle r="10" fill="#fff" stroke="var(--ink)" stroke-width="1.6"/><path d="M-6 -8 Q-2 0 -6 8 M6 -8 Q2 0 6 8" fill="none" stroke="var(--ink)" stroke-width="1.2" stroke-dasharray="2 1.5"/></g>
      <g id="t4"><use href="#disc"/></g>
      <g id="t5"><use href="#disc"/><rect x="-8" y="-10" width="16" height="20" rx="1" fill="var(--ink)"/><rect x="-8" y="7" width="16" height="2" fill="#fff"/></g>
      <g id="t6"><use href="#disc"/><circle r="10" fill="#fff" stroke="var(--ink)" stroke-width="1.6"/><path d="M0 -4 L4 -1 L2.5 4 L-2.5 4 L-4 -1 Z" fill="var(--ink)"/><path d="M0 -4 V-10 M4 -1 L9.5 -3 M2.5 4 L6 8.5 M-2.5 4 L-6 8.5 M-4 -1 L-9.5 -3" stroke="var(--ink)" stroke-width="1.2"/></g>
      <g id="t7"><use href="#disc"/></g>
      <g id="t8"><use href="#disc"/><circle r="10" fill="var(--ink)"/><path d="M-10 0 H10 M0 -10 V10 M-7 -7 Q-2 0 -7 7 M7 -7 Q2 0 7 7" fill="none" stroke="#fff" stroke-width="1"/></g>
      <g id="t9"><use href="#disc"/><circle cx="-3" cy="1" r="8" fill="none" stroke="var(--ink)" stroke-width="1.4"/><circle cx="9" cy="6" r="3" fill="none" stroke="var(--ink)" stroke-width="1.4"/><path d="M-3 -7 L-6 -10 M-3 1 L9 6" stroke="var(--ink)" stroke-width="1.2"/></g>
      <g id="t10"><use href="#disc"/></g>
      <g id="t11"><use href="#disc"/><path d="M-10 9 H10 Q10 -11 0 -11 Q-10 -11 -10 9 Z" fill="var(--ink)"/><path d="M-10 4 H10 M-9 -1 H9 M-7 -6 H7" stroke="#fff" stroke-width="1.3"/></g>

      <g id="tokenRow">
        <use href="#t0" x="0"/><use href="#t1" x="54"/><use href="#t2" x="108"/><use href="#t3" x="162"/>
        <use href="#t4" x="216"/><use href="#t5" x="270"/><use href="#t6" x="324"/><use href="#t7" x="378"/>
        <use href="#t8" x="432"/><use href="#t9" x="486"/><use href="#t10" x="540"/><use href="#t11" x="594"/>
        <use href="#t0" x="648"/><use href="#t1" x="702"/><use href="#t2" x="756"/><use href="#t3" x="810"/>
        <use href="#t4" x="864"/><use href="#t5" x="918"/><use href="#t6" x="972"/><use href="#t7" x="1026"/>
        <use href="#t8" x="1080"/><use href="#t9" x="1134"/><use href="#t10" x="1188"/><use href="#t11" x="1242"/>
      </g>
    </defs>

    <!-- header band -->
    <path d="M0 0 H740 V176 Q520 236 370 232 Q160 228 0 196 Z" fill="url(#navyBand)"/>
    <path d="M0 204 Q160 236 370 240 Q520 244 740 184" fill="none" stroke="var(--silver-dark)" stroke-width="5"/>

    <!-- activity grid -->
    <g class="activity-grid" clip-path="url(#gridClip)">
      <use href="#tokenRow" x="70" y="275"/>
      <use href="#tokenRow" x="16" y="327"/>
      <use href="#tokenRow" x="-38" y="379"/>
      <use href="#tokenRow" x="-92" y="431"/>
      <use href="#tokenRow" x="-146" y="483"/>
      <use href="#tokenRow" x="-200" y="535"/>
      <use href="#tokenRow" x="-254" y="587"/>
      <use href="#tokenRow" x="-308" y="639"/>
      <use href="#tokenRow" x="-362" y="691"/>
      <use href="#tokenRow" x="-416" y="743"/>
      <use href="#tokenRow" x="-470" y="795"/>
      <use href="#tokenRow" x="-524" y="847"/>
    </g>

    <!-- footer band -->
    <path d="M0 888 Q370 930 740 888" fill="none" stroke="var(--silver-dark)" stroke-width="5"/>
    <path d="M0 896 Q370 938 740 896 V1040 H0 Z" fill="url(#navyBand)"/>
  </svg>

  <div class="city-mark">
    <div class="city-mark__circle"></div>
    <span class="city-mark__name">City of Ashford Vale</span>
  </div>

  <h1 class="title">
    <span class="title__year">2020 Activity</span>
    <span class="title__sub">Guide</span>
  </h1>

  <p class="footer-heading">Stay Connected</p>

  <p class="contact-pill contact-pill--web">
    <svg viewBox="0 0 16 16" aria-hidden="true"><circle cx="8" cy="8" r="6.5" fill="none" stroke="#111" stroke-width="1.3"/><path d="M1.5 8 H14.5 M8 1.5 Q4 8 8 14.5 Q12 8 8 1.5" fill="none" stroke="#111" stroke-width="1.1"/></svg>
    www.ashfordvale-ca.gov
  </p>
  <p class="contact-pill contact-pill--phone">
    <svg viewBox="0 0 16 16" aria-hidden="true"><circle cx="8" cy="8" r="7" fill="none" stroke="#111" stroke-width="1.2"/><path d="M5.2 4.2 L6.6 4 L7.3 6 L6.4 6.8 Q7.2 8.6 9.1 9.6 L9.9 8.7 L11.9 9.4 L11.7 10.8 Q8.6 11.4 6.4 9.3 Q4.4 7.2 5.2 4.2 Z" fill="#111"/></svg>
    (909) 555-0142
  </p>
</main>
</body>
</html>
```